Letterhead and Business card for Construction company

We need a letterhead and business card with our new company logo. We are based in NY. We develop and build properties.

The design should incorporate some unique feature from the logo (shape, font...). it should look like an extension from it.

Design should be clean and elegant, professional, not too busy.

The letterhead should include:
Logo (attached)
Address
Phone
Email

Please find the attached logo images and AI file.

Target Market(s)

Construction industry professionals

Industry/Entity Type

Construction, Development

Font styles to use
Sans Serif

Colors

Designer to choose colors to be used in the design.

Requirements
Must have
• Design should incorporate logo elements, additional assets are welcome. I'd like to see some other shapes / images invorporated too.

```html
<!DOCTYPE html>
<html lang="en">
<head>
<meta charset="utf-8">
<title>Halvern Builders Letterhead</title>
<link href="https://fonts.googleapis.com/css2?family=Arimo:wght@400&family=Mulish:wght@600;700;800&display=swap" rel="stylesheet">
<style>
  :root {
    --backdrop: #9c9b9c;
    --paper: #ffffff;
    --ink: #1f1c1c;
    --text: #4a4a4a;
    --accent: #f08a2c;
    --faint-grey: #e8e7e8;
    --faint-peach: #fdf0e7;
  }
  * { margin: 0; padding: 0; box-sizing: border-box; }
  html, body { width: 960px; height: 1200px; overflow: hidden; background: var(--backdrop); }
  .letterhead {
    position: absolute; left: 70px; top: 20px;
    width: 820px; height: 1160px;
    background: var(--paper); overflow: hidden;
    font-family: "Arimo", Arial, sans-serif; color: var(--text);
  }
  .brand {
    position: absolute; left: 73px; top: 92px;
    display: flex; align-items: center; gap: 10px;
  }
  .brand-mark { width: 22px; height: 22px; background: var(--accent); }
  .brand-name {
    font-family: "Mulish", sans-serif; font-weight: 800;
    font-size: 26px; letter-spacing: 0.5px; color: var(--ink);
  }
  .contact {
    position: absolute; left: 588px; top: 55px;
    font-size: 13.5px; line-height: 17px; color: var(--ink);
  }
  .contact-address { margin-bottom: 9px; }
  .contact-row { display: flex; align-items: center; gap: 7px; }
  .contact-row svg { width: 12px; height: 12px; flex: none; }
  .header-rule {
    position: absolute; left: 73px; top: 161px;
    width: 672px; height: 2px; background: var(--accent);
  }
  .salutation {
    position: absolute; left: 75px; top: 355px;
    font-family: "Mulish", sans-serif; font-weight: 700;
    font-size: 18.5px; color: var(--text);
  }
  .letter-body {
    position: absolute; left: 73px; top: 409px; width: 672px;
    font-size: 14px; line-height: 16.9px;
  }
  .letter-body p { margin-bottom: 14.5px; }
  .faint-block {
    position: absolute; left: 0; top: 900px;
    width: 230px; height: 260px; background: var(--faint-grey);
  }
  .closing {
    position: absolute; left: 74px; top: 756px;
    font-family: "Mulish", sans-serif; font-weight: 700;
    font-size: 11px; color: var(--text);
  }
  .signature {
    position: absolute; left: 74px; top: 796px;
    width: 134px; height: 40px;
    background: linear-gradient(90deg, #d9d9d9, #eeeeee);
  }
</style>
</head>
<body>
  <main class="letterhead">
    <div class="faint-block" aria-hidden="true"></div>

    <header>
      <div class="brand">
        <span class="brand-mark"></span>
        <span class="brand-name">HALVERN BUILDERS</span>
      </div>

      <address class="contact" style="font-style:normal">
        <div class="contact-address">Your address, city<br>state, ZIP 0000</div>
        <div class="contact-row">
          <svg viewBox="0 0 12 12"><path d="M2.5 1l2 2.2-1 1.3c.7 1.5 1.9 2.7 3.4 3.4l1.3-1L10.4 9l-1 1.6C5.4 10.5 1.5 6.6 1.4 2.6z" fill="var(--accent)"/></svg>
          <span>123-456-2100</span>
        </div>
        <div class="contact-row">
          <svg viewBox="0 0 12 12"><rect x="1" y="2.5" width="10" height="7" fill="none" stroke="var(--accent)" stroke-width="1"/><path d="M1 2.8l5 3.8 5-3.8" fill="none" stroke="var(--accent)" stroke-width="1"/></svg>
          <span>youremail@example.com</span>
        </div>
        <div class="contact-row">
          <svg viewBox="0 0 12 12"><circle cx="6" cy="6" r="4.7" fill="none" stroke="var(--accent)" stroke-width="0.9"/><ellipse cx="6" cy="6" rx="2" ry="4.7" fill="none" stroke="var(--accent)" stroke-width="0.9"/><path d="M1.3 6h9.4" stroke="var(--accent)" stroke-width="0.9"/></svg>
          <span>www.yourwebsite.com</span>
        </div>
      </address>

      <div class="header-rule"></div>
    </header>

    <h1 class="salutation">Dear Mr. Smith,</h1>

    <section class="letter-body">
      <p>Lorem ipsum dolor sit amet, consectetuer adipiscing elit, sed diam nonmmy nibh euismod tincidunt ut laor eet dolore magna aliquam erat volutpat. Ut wisi enim ad minim veniam, quis nostrud exerci tationmcorper suscipit lobortis nisl ut aliquip ex ea commodo consequat. Duis autem vel eum iriure dolor in hendrerit in vulputate velit esse molestie consequat, vel illum dolore eu feugiat</p>
      <p>Rorem ipsum dolor sit amet, consectetuer adipiscing elit, sed diam nonmmy nibh euismod tincidunt ut laor eet dolore magna aliquam erat volutpat. Ut wisi enim ad minim veniam, quis nostrud exerci tationmcorper suscipit lobortis nisl ut aliquip ex ea commodo consequat. Duis autem vel eum iriure dolor in hendrerit in vulputate velit esse molest</p>
      <p>Dorem ipsum dolor sit amet, consectetuer adipiscing elit, sed diam nonmmy nibh euismod tincidunt ut laor eet dolore magna aliquam erat volutpat. Ut wisi enim ad minim veniam, quis nostrud exerci tationmcorper suscipit lobortis nisl ut aliquip ex ea commodo consequat. Duis autem vel eum iriure dolor in hendrerit in suscipit lobortis nisl ut aliquip ex ea commodo consequat. Duis autem vel eum iriure dolor in hendrerit in vulputate velit esse molestie consequat, vel illum</p>
      <p>Sorem ipsum dolor sit amet, consectetuer adipiscing elit, sed diam nonmmy nibh euismod tincidunt ut laor eet dolore magna aliquam erat volutpat. Ut wisi enim ad minim veniam, quis nostrud exerci tationmcorper suscipit lobortis nisl ut aliquip ex ea commodo consequat. Duis autem vel eum iriure dolor in</p>
    </section>

    <footer>
      <div class="closing">Sincerely,</div>
      <div class="signature" role="img" aria-label="Handwritten signature of the sender"></div>
    </footer>
  </main>
</body>
</html>
```